Consulting/ Manufacturers Representative Website

I need a website for a consulting/manufacturer representative company in Texas called Birchwell Venture Advisors. We Uncover and implement the right solution, at the right time, in the right way. We consult, we train, we offer project management, we offer performance improvement, we offer value creation, we turn stagnation into growth, and we offer corporate performance improvement.
I want the design to load on desktop and mobile, I want the site to look and feel professional like a large firm, and I want the site to be a marketing tool and establish a strong online presence.

Target Market(s)

City Governments, State Governments, County Governments, US Government, Power Plants, Refineries, Chemical Plants, Industrial customers

Industry/Entity Type

Consulting

Number of Pages Required

5+ page

Requirements
Must have
• mobile and desktop compatible, professional look, must be a fast website, company email and contact capabilities, contact page, company logo on website, SEO optimized, must display different industries served: Energy, Public (Government, Not For Profit, Educational), Transportation & Logistics, Business Services.
• Show that I help customers operate in a cleaner, safer and more economical way.
Nice to have
• news letter, news feed, show that company is principles based.
Should not have
• slow site, cheap look

```html
<!DOCTYPE html>
<html lang="en">
<head>
<meta charset="utf-8">
<title>Birchwell Venture Advisors</title>
<link href="https://fonts.googleapis.com/css2?family=Playfair+Display:wght@700&family=Roboto:wght@400;500;700&display=swap" rel="stylesheet">
<style>
:root{
  --ink:#111111;
  --dark:#1b1b1b;
  --grey-text:#555555;
  --muted:#9a9a9a;
  --line:#e3e3e3;
  --white:#ffffff;
  --card-shadow:0 3px 10px rgba(0,0,0,.16);
}
*{margin:0;padding:0;box-sizing:border-box}
html,body{width:1200px;height:4276px;overflow:hidden}
body{font-family:"Roboto",Arial,sans-serif;color:var(--ink);background:var(--white);position:relative}
.heading{font-family:"Playfair Display",Georgia,serif;font-weight:700;letter-spacing:4px;text-transform:uppercase}
.btn{display:inline-flex;align-items:center;justify-content:center;background:var(--ink);color:var(--white);font-size:13px;letter-spacing:2px;text-transform:uppercase;text-decoration:none;height:42px;width:242px}
section,header,footer{position:absolute;left:0;width:1200px}

/* Header */
.site-header{top:0;height:171px;background:var(--white)}
.brand{position:absolute;left:88px;top:22px;width:150px;text-align:center;font-family:"Playfair Display",Georgia,serif;font-weight:700;color:var(--ink);line-height:1.05}
.brand .mark{display:block;width:34px;height:34px;border:2px solid var(--ink);margin:0 auto 10px}
.brand .name{font-size:24px;letter-spacing:3px;display:block}
.brand .sub{font-size:10.5px;letter-spacing:1.8px;display:block;margin-top:3px}
.top-contacts{position:absolute;right:88px;top:28px;display:flex;gap:38px;font-size:15px;color:var(--grey-text)}
.top-contacts span{display:flex;align-items:center;gap:12px}
.top-contacts .ico{width:30px;height:30px;border-radius:50%;background:var(--ink);display:flex;align-items:center;justify-content:center}
.top-line{position:absolute;left:540px;right:88px;top:80px;border-top:1px solid var(--line)}
.main-nav{position:absolute;right:88px;top:116px;display:flex;gap:50px;font-size:14px;letter-spacing:1.5px;text-transform:uppercase;color:var(--muted)}
.main-nav a{color:inherit;text-decoration:none;padding-bottom:20px}
.main-nav a.active{color:var(--ink);border-bottom:2px solid var(--ink)}

/* Hero */
.hero{top:171px;height:530px;background:linear-gradient(180deg,#5d6266 0%,#3c3f42 55%,#4a3a2e 85%,#2e2620 100%)}
.hero-text{position:absolute;left:0;width:100%;top:243px;text-align:center;color:var(--white)}
.hero-text .kicker{font-size:30px;letter-spacing:6px}
.hero-text h1{font-size:46px;letter-spacing:6px;margin-top:2px}
.hero-text p{font-size:22px;margin-top:16px}
.hero-text .btn{margin-top:26px}

/* About */
.about{top:701px;height:482px}
.about h2{position:absolute;left:177px;top:105px;font-size:36px}
.about p{position:absolute;left:177px;top:170px;width:400px;font-size:13.5px;line-height:24px;color:var(--grey-text)}
.about .btn{position:absolute;left:177px;top:322px}
.about .photo{position:absolute;left:644px;top:89px;width:382px;height:302px;background:linear-gradient(135deg,#a9c0d6,#4d6f90 50%,#cfdce8);box-shadow:0 12px 26px rgba(0,0,0,.35)}

/* Offer */
.offer{top:1183px;height:789px;background:var(--dark);color:var(--white)}
.offer h2{position:absolute;top:75px;width:100%;text-align:center;font-size:36px}
.offer .tag{position:absolute;top:140px;width:100%;text-align:center;font-size:15px;letter-spacing:3.5px;line-height:29px;text-transform:uppercase;color:#d9d9d9}
.offer svg.ring{position:absolute;left:0;top:0}
.service{position:absolute;width:300px;font-size:13px;line-height:24px;color:#bdbdbd}
.service h3{font-size:15px;letter-spacing:1.2px;color:var(--white);font-weight:700;margin-bottom:4px}
.service.right{text-align:left}
.service.left{text-align:center}
.hub-name{position:absolute;left:511px;top:360px;width:180px;text-align:center;font-family:"Playfair Display",Georgia,serif;font-weight:700;font-size:16px;letter-spacing:3px;color:var(--white)}

/* Served */
.served{top:1972px;height:912px}
.served h2{position:absolute;top:75px;width:100%;text-align:center;font-size:36px}
.served .intro{position:absolute;top:150px;left:88px;width:1024px;text-align:center;font-size:13.5px;line-height:28px;color:var(--grey-text)}
.card{position:absolute;width:234px;height:282px;background:var(--white);box-shadow:var(--card-shadow);text-align:center}
.card svg{display:block;margin:52px auto 0}
.card h3{font-size:15px;letter-spacing:.6px;margin-top:22px;font-weight:700}
.card p{font-size:13.5px;line-height:26px;color:var(--grey-text);margin:10px 28px 0}

/* Help band */
.help{top:2884px;height:365px;background:linear-gradient(135deg,#8e9499 0%,#6f757a 45%,#9aa0a4 100%)}
.help h2{position:absolute;top:80px;width:100%;text-align:center;font-size:36px;color:var(--white)}
.help .points{position:absolute;top:160px;left:88px;width:1024px;display:flex;justify-content:space-between}
.help .point{display:flex;align-items:center;gap:22px;color:var(--white);font-size:15px;font-weight:700;letter-spacing:1.2px;text-transform:uppercase}
.help .btn{position:absolute;left:479px;top:242px}

/* News */
.news{top:3249px;height:627px}
.news h2{position:absolute;top:75px;width:100%;text-align:center;font-size:36px}
.post{position:absolute;top:145px;width:322px;height:382px;background:var(--white);box-shadow:var(--card-shadow)}
.post .thumb{height:205px}
.post h3{font-size:15px;letter-spacing:.8px;margin:24px 16px 0;font-weight:700}
.post .date{font-size:11px;color:var(--muted);margin:8px 16px 0}
.post p{font-size:13.5px;line-height:26px;color:var(--grey-text);margin:14px 16px 0}
.post.feature{background:linear-gradient(180deg,#c7a37c 0%,#7d5b3f 50%,#3b2a20 100%)}
.post.feature .caption{position:absolute;left:16px;bottom:30px;color:var(--white)}
.post.feature h3{margin:0}
.post.feature .date{margin:8px 0 0;color:#e0d6cc}

/* Footer */
.site-footer{top:3876px;height:400px;background:#000;color:var(--white)}
.to-top{position:absolute;right:80px;top:-14px;width:36px;height:36px;background:var(--white);border:2px solid #000;display:flex;align-items:center;justify-content:center}
.site-footer .brand{left:88px;top:80px;color:var(--white)}
.site-footer .brand .mark{border-color:var(--white)}
.f-col{position:absolute;top:97px;font-size:13px;color:#cfcfcf}
.f-col h4{font-size:14px;letter-spacing:1.5px;color:var(--white);font-weight:500;margin-bottom:18px}
.f-col li{list-style:none;line-height:25px}
.f-col .row{display:flex;gap:14px;line-height:21px;margin-bottom:12px}
.f-col input{display:block;width:243px;height:43px;background:transparent;border:1px solid #777;color:#aaa;padding:0 14px;font-size:12px}
.f-col .subscribe{display:flex;align-items:center;justify-content:center;width:243px;height:43px;background:var(--white);color:var(--ink);font-size:13px;letter-spacing:1.5px;margin-top:14px}
.f-bottom{position:absolute;left:88px;right:88px;top:330px;border-top:1px solid #333;padding-top:28px;display:flex;justify-content:space-between;font-size:12px;color:#bdbdbd}
.social{display:flex;gap:18px}
.social span{width:12px;height:12px;border-radius:50%;background:var(--white)}
</style>
</head>
<body>

<header class="site-header">
  <div class="brand"><span class="mark"></span><span class="name">BIRCHWELL</span><span class="sub">VENTURE ADVISORS</span></div>
  <div class="top-contacts">
    <span><i class="ico"><svg width="14" height="14" viewBox="0 0 24 24"><path fill="#fff" d="M6.6 10.8a15 15 0 006.6 6.6l2.2-2.2c.3-.3.7-.4 1-.2 1.1.4 2.3.6 3.6.6.6 0 1 .4 1 1V20c0 .6-.4 1-1 1A17 17 0 013 4c0-.6.4-1 1-1h3.5c.6 0 1 .4 1 1 0 1.3.2 2.5.6 3.6.1.3 0 .7-.2 1z"/></svg></i>555 014 2270</span>
    <span><i class="ico"><svg width="14" height="14" viewBox="0 0 24 24"><path fill="#fff" d="M3 5h18v14H3z"/><path fill="none" stroke="#111" stroke-width="2" d="M3 6l9 7 9-7"/></svg></i>info@birchwelladvisors.com</span>
  </div>
  <div class="top-line"></div>
  <nav class="main-nav">
    <a class="active" href="#">Home</a><a href="#">About Us</a><a href="#">Offers</a><a href="#">News</a><a href="#">Contact Us</a>
  </nav>
</header>

<section class="hero" role="img" aria-label="Photo of business team meeting around a boardroom table">
  <div class="hero-text">
    <div class="kicker heading">Welcome to</div>
    <h1 class="heading">Birchwell Venture Advisors</h1>
    <p>We are consulting/manufacturer representative company in Texas</p>
    <a class="btn" href="#">Keep in touch</a>
  </div>
</section>

<section class="about">
  <h2 class="heading">About Us</h2>
  <p>Lorem Ipsum is simply dummy text of the printing and typesetting industry. Lorem Ipsum has been the industry's standard dummy text ever since the 1500s, when an unknown printer took a galley of type and scrambled it to make a type specimen book. It has survived</p>
  <a class="btn" href="#">Read more</a>
  <div class="photo" role="img" aria-label="Photo of a glass office tower seen from below"></div>
</section>

<section class="offer">
  <h2 class="heading">What We Offer</h2>
  <div class="tag">We uncover and implement the right solution,<br>at the right time, in the right way.</div>
  <svg class="ring" width="1200" height="789" viewBox="0 0 1200 789">
    <path d="M393 272 A227 227 0 1 0 810 272" fill="none" stroke="#fff" stroke-width="3"/>
    <g fill="#1b1b1b" stroke="#fff" stroke-width="3">
      <circle cx="393" cy="270" r="32"/><circle cx="810" cy="270" r="32"/>
      <circle cx="411" cy="465" r="32"/><circle cx="795" cy="465" r="32"/>
      <circle cx="601" cy="572" r="32"/>
    </g>
    <g fill="none" stroke="#fff" stroke-width="2.5" stroke-linecap="round" stroke-linejoin="round">
      <path d="M381 282v-14l6-6 6 6 6-10 6 4M381 282h24"/>
      <path d="M798 272h24M810 260v24M800 262l20 20"/>
      <path d="M399 477h24M402 477v-8M409 477v-13M416 477v-18M402 462l14-12"/>
      <path d="M785 476l8-12 6 6 8-14M786 478h20"/>
      <path d="M589 584v-22h24v22M594 568h4M604 568h4M594 576h4M604 576h4M586 584h30"/>
    </g>
  </svg>
  <div class="hub-name">BIRCHWELL</div>
  <div class="service left" style="left:88px;top:224px"><h3>PROJECT MANAGEMENT</h3>Lorem Ipsum is simply dummy text of<br>the printing and typesetting industry.</div>
  <div class="service right" style="left:876px;top:224px"><h3>VALUE CREATION</h3>Lorem Ipsum is simply dummy text of<br>the printing and typesetting industry.</div>
  <div class="service left" style="left:70px;top:418px"><h3>PERFORMANCE IMPROVEMENT</h3>Lorem Ipsum is simply dummy text of<br>the printing and typesetting industry.</div>
  <div class="service right" style="left:869px;top:418px"><h3>STAGNATION INTO GROWTH</h3>Lorem Ipsum is simply dummy text of<br>the printing and typesetting industry.</div>
  <div class="service left" style="left:401px;top:630px;width:400px"><h3>CORPORATE PERFORMANCE IMPROVEMENT</h3>Lorem Ipsum is simply dummy text of<br>the printing and typesetting industry.</div>
</section>

<section class="served">
  <h2 class="heading">Whom We Served</h2>
  <p class="intro">Lorem Ipsum is simply dummy text of the printing and typesetting industry. Lorem Ipsum has been the industry's standard dummy text ever since the 1500s, when an unknown printer took a galley of type and scrambled it to make a type specimen book. It has survived.</p>

  <div class="card" style="left:88px;top:228px">
    <svg width="64" height="70" viewBox="0 0 64 70" fill="none" stroke="#666" stroke-width="2.5"><path d="M6 68V30h16v38M22 68V8h20v60M42 68V24h16v44M2 68h60M28 16h8M28 26h8M28 36h8M28 46h8M10 38h8M10 48h8M46 32h8M46 42h8"/></svg>
    <h3>CITY GOVERNMENT</h3><p>Lorem Ipsum is simply dummy text of the printing and typesetting industry.</p>
  </div>
  <div class="card" style="left:351px;top:228px">
    <svg width="70" height="70" viewBox="0 0 70 70" fill="none" stroke="#666" stroke-width="2.5"><path d="M6 30h58L35 12zM35 12V4h8M10 30v30M60 30v30M4 60h62v6H4zM20 36v18M30 36v18M40 36v18M50 36v18"/></svg>
    <h3>STATE GOVERNMENT</h3><p>Lorem Ipsum is simply dummy text of the printing and typesetting industry.</p>
  </div>
  <div class="card" style="left:613px;top:228px">
    <svg width="70" height="70" viewBox="0 0 70 70" fill="none" stroke="#666" stroke-width="2.5"><path d="M8 26h54L35 8zM35 8V2M14 26v32M56 26v32M24 32v22M35 32v22M46 32v22M6 58h58v8H6z"/></svg>
    <h3>COUNTY GOVERNMENT</h3><p>Lorem Ipsum is simply dummy text of the printing and typesetting industry.</p>
  </div>
  <div class="card" style="left:875px;top:228px">
    <svg width="70" height="70" viewBox="0 0 70 70" fill="none" stroke="#666" stroke-width="2.5"><path d="M22 24a13 13 0 0126 0zM35 11V3M14 24h42v36H14zM22 32v20M30 32v20M40 32v20M48 32v20M8 60h54v6H8z"/></svg>
    <h3>US GOVERNMENT</h3><p>Lorem Ipsum is simply dummy text of the printing and typesetting industry.</p>
  </div>

  <div class="card" style="left:88px;top:539px">
    <svg width="70" height="70" viewBox="0 0 70 70" fill="none" stroke="#666" stroke-width="2.5"><path d="M4 66h62M8 66V40l12-8v8l12-8v8l12-8v34M50 66l4-50h6l4 50M46 16l12-12 10 10M54 30h10"/></svg>
    <h3>POWER PLANTS</h3><p>Lorem Ipsum is simply dummy text of the printing and typesetting industry.</p>
  </div>
  <div class="card" style="left:351px;top:539px">
    <svg width="70" height="70" viewBox="0 0 70 70" fill="none" stroke="#666" stroke-width="2.5"><path d="M4 66h62M10 66V20a6 6 0 0112 0v46M29 66V14a6 6 0 0112 0v52M48 66V20a6 6 0 0112 0v46M10 36h50M10 50h50"/></svg>
    <h3>REFINERIES</h3><p>Lorem Ipsum is simply dummy text of the printing and typesetting industry.</p>
  </div>
  <div class="card" style="left:613px;top:539px">
    <svg width="70" height="70" viewBox="0 0 70 70" fill="none" stroke="#666" stroke-width="2.5"><path d="M14 4h14M18 4v22L6 56a6 6 0 006 8h18a6 6 0 006-8L24 26V4M10 46h22M44 66h22M55 66V40M55 40a7 7 0 10.1 0"/></svg>
    <h3>CHEMICAL PLANTS</h3><p>Lorem Ipsum is simply dummy text of the printing and typesetting industry.</p>
  </div>
  <div class="card" style="left:875px;top:539px">
    <svg width="70" height="70" viewBox="0 0 70 70" fill="none" stroke="#666" stroke-width="2.5"><path d="M4 66h62M6 66V36l16-10v10l16-10v10l16-10V6h8v60M14 48h6M28 48h6M42 48h6"/></svg>
    <h3>INDUSTRIAL CUSTOMERS</h3><p>Lorem Ipsum is simply dummy text of the printing and typesetting industry.</p>
  </div>
</section>

<section class="help" role="img" aria-label="Photo of a desk with laptop, phone, glasses and coffee cup">
  <h2 class="heading">We Help You</h2>
  <div class="points">
    <div class="point"><svg width="46" height="46" viewBox="0 0 46 46" fill="none" stroke="#fff" stroke-width="2.5"><path d="M34 4H4v38h38V22"/><path d="M12 22l10 10L44 6"/></svg>Operate in a cleaner way</div>
    <div class="point"><svg width="46" height="46" viewBox="0 0 46 46" fill="none" stroke="#fff" stroke-width="2.5"><path d="M34 4H4v38h38V22"/><path d="M12 22l10 10L44 6"/></svg>Operate in a safer way</div>
    <div class="point"><svg width="46" height="46" viewBox="0 0 46 46" fill="none" stroke="#fff" stroke-width="2.5"><path d="M34 4H4v38h38V22"/><path d="M12 22l10 10L44 6"/></svg>And more economical way</div>
  </div>
  <a class="btn" href="#">Keep in touch</a>
</section>

<section class="news">
  <h2 class="heading">Latest News</h2>
  <article class="post" style="left:88px">
    <div class="thumb" role="img" aria-label="Photo of colleagues in a meeting room" style="background:linear-gradient(135deg,#d8dde2,#7d8a98 55%,#3e4a5a)"></div>
    <h3>LOREM IPSUM DOLOR SIT AMET</h3><div class="date">Dated: 10th May, 2018</div>
    <p>It is a long established fact that a reader will be distracted by the readable content of a page when looking at its layout.</p>
  </article>
  <article class="post" style="left:439px">
    <div class="thumb" role="img" aria-label="Photo of businessmen in conversation" style="background:linear-gradient(135deg,#e9eef3,#9aa8b6 50%,#2f3742)"></div>
    <h3>LOREM IPSUM DOLOR SIT AMET</h3><div class="date">Dated: 10th May, 2018</div>
    <p>It is a long established fact that a reader will be distracted by the readable content of a page when looking at its layout.</p>
  </article>
  <article class="post feature" style="left:790px" role="img" aria-label="Photo of business people silhouetted against office windows">
    <div class="caption"><h3>LOREM IPSUM DOLOR SIT AMET</h3><div class="date">Dated: 10th May, 2018</div></div>
  </article>
</section>

<footer class="site-footer">
  <div class="to-top"><svg width="16" height="12" viewBox="0 0 16 12"><path d="M2 10l6-6 6 6" fill="none" stroke="#000" stroke-width="3"/></svg></div>
  <div class="brand"><span class="mark"></span><span class="name">BIRCHWELL</span><span class="sub">VENTURE ADVISORS</span></div>
  <div class="f-col" style="left:351px">
    <h4>SITEMAP</h4>
    <ul><li>Home</li><li>About us</li><li>Offers</li><li>News</li><li>Contact us</li></ul>
  </div>
  <div class="f-col" style="left:544px">
    <h4>CONTACT INFO</h4>
    <div class="row"><svg width="12" height="16" viewBox="0 0 12 16"><path fill="#fff" d="M6 0a6 6 0 016 6c0 4-6 10-6 10S0 10 0 6a6 6 0 016-6zm0 4a2 2 0 100 4 2 2 0 000-4z"/></svg><span>48 Alder Street, Suite 200,<br>Austin, TX 73301</span></div>
    <div class="row"><svg width="14" height="14" viewBox="0 0 24 24"><path fill="#fff" d="M6.6 10.8a15 15 0 006.6 6.6l2.2-2.2c.3-.3.7-.4 1-.2 1.1.4 2.3.6 3.6.6.6 0 1 .4 1 1V20c0 .6-.4 1-1 1A17 17 0 013 4c0-.6.4-1 1-1h3.5c.6 0 1 .4 1 1 0 1.3.2 2.5.6 3.6.1.3 0 .7-.2 1z"/></svg><span>555 014 2270 | 555 014 2291</span></div>
    <div class="row"><svg width="14" height="12" viewBox="0 0 14 12"><rect width="14" height="12" fill="#fff"/><path d="M0 1l7 5 7-5" fill="none" stroke="#000" stroke-width="1.5"/></svg><span>info@birchwelladvisors.com</span></div>
  </div>
  <div class="f-col" style="left:869px">
    <h4>SUBSCRIBE OUR NEWSLETTER</h4>
    <input type="text" value="Email..." aria-label="Email">
    <div class="subscribe">SUBSCRIBE</div>
  </div>
  <div class="f-bottom">
    <span>Copyright © 2018 | All Rights Reserved</span>
    <div class="social"><span></span><span></span><span></span><span></span></div>
  </div>
</footer>

</body>
</html>
```